Start-up lawncare company needing marketing flyer to promote business model

Hello! We are looking for a marketing flyer design with the requirements below.

We would like the size to fit a flyer that is 6.25" X 9", Front and Back.

We need these to meet the NPDS RCMX requirements, there are details attached for the indicias that need to be included, and where to put them on the back of the flyer.

Here's the items items we would like to have included on the flyer:
- Logo (Attached)

- I attached a snip of how our website looks, as well as how our app looks, and would like to follow that general color scheme

- References to our YardMint App, in both Quorvex and Plinth stores, and our website (www.YardMint.example)

- Reference to the neighborhood barometer and gets the point across that the more of their neighbors that sign up, the cheaper the price of service (Visual attached of what this barometer looks like)

- We are licensed and insured landscaping pros

- Real, instant, upfront pricing for mowing, mulching and most other services

- Sign up with a few easy steps and manage your account from our app or online

- Automated safe & secure transactions upon service completion and satisfaction

- Excellent customer service with our quality guaranteed commitment!

- Sign up now and receive 50% off your first mow!

- Veteran owned

- A portion of our proceeds go to "Rowan Ellery Foundation"

- List's out all of the services we will offer
- Mowing
- Mulching
- Aeration and Over-seeding
- Fertilization
- Shrub/Tree Trimming
- Leaf removal and yard clean up
- Accent lighting installation
- Sprinkler blow-out / Winterization
- Driveway pressure washing and sealing
- Firewood Delivery

Target Market(s)

Homeowners in large neighborhoods that need lawn care services

Industry/Entity Type

Lawn Care

Font styles to use
Sans Serif

Colors

Designer to choose colors to be used in the design.

Requirements
Must have
• Meet NPDS RCMX requirements
• Keep a similar color scheme to our website, feel free to use bold accents to make it more eye-catching as people search through their mail
• Get the general point across that as more of their neighbors sign up with us, the cheaper their service will be

```html
<!DOCTYPE html>
<html lang="en">
<head>
<meta charset="utf-8">
<title>YardMint Mailer – Front and Back</title>
<link rel="stylesheet" href="https://fonts.googleapis.com/css2?family=Montserrat:wght@400;500;600;700;800&family=Arimo:wght@400;700&display=swap">
<style>
  :root {
    --navy: #2f4f8e;
    --green: #5cb85c;
    --green-bright: #62b956;
    --teal: #3ba7b4;
    --cyan: #2bb0e4;
    --white: #ffffff;
    --ink: #222222;
    --pale: #e6f7c9;
    --copper: #c9a088;
    --silver: #cfd0d3;
    --gold: #eec37a;
    --bg: #e4e4e4;
  }
  * { box-sizing: border-box; margin: 0; padding: 0; }
  html, body { width: 781px; height: 1200px; overflow: hidden; }
  body {
    background: var(--bg);
    font-family: "Montserrat", Arial, sans-serif;
    position: relative;
  }
  .card { position: absolute; left: 40px; width: 700px; overflow: hidden; }

  /* ---------- front ---------- */
  .front { top: 92px; height: 486px; background: var(--white); }
  .front-hero {
    position: absolute; left: 0; top: 0; width: 700px; height: 270px;
    background: var(--navy);
  }
  .front-headline {
    position: absolute; left: 54px; top: 34px;
    color: var(--white); font-weight: 600; line-height: 1.2;
  }
  .front-headline .line-1 { display: block; font-size: 31px; }
  .front-headline .line-2 { display: block; font-size: 38px; margin-top: 2px; }
  .front-intro {
    position: absolute; left: 54px; top: 154px; width: 446px;
    color: var(--white); font-size: 11.6px; line-height: 20.6px;
  }
  .front-intro strong { font-weight: 700; }
  .front-stripe {
    position: absolute; left: 0; top: 273px; width: 700px; height: 6px;
    background: var(--cyan);
  }
  .front-band {
    position: absolute; left: 0; top: 286px; width: 700px; height: 200px;
    background: linear-gradient(100deg, var(--green) 10%, #4db182 55%, var(--teal) 100%);
  }
  .brand-lockup {
    position: absolute; display: flex; align-items: center; gap: 8px;
    color: var(--white); font-weight: 800;
  }
  .brand-lockup .dot { background: var(--white); border-radius: 50%; flex: none; }
  .front-band .brand-lockup { left: 44px; top: 80px; font-size: 34px; }
  .front-band .brand-lockup .dot { width: 20px; height: 20px; }
  .front-web {
    position: absolute; left: 253px; top: 76px;
    color: var(--white); font-size: 13px; font-weight: 600;
  }
  .store-badge {
    position: absolute; top: 101px; width: 72px; height: 21px;
    background: #111; border: 1px solid #555; border-radius: 3px;
    color: var(--white); font-size: 8.5px; font-weight: 600;
    display: flex; align-items: center; justify-content: center;
  }
  .store-badge.plinth { left: 253px; }
  .store-badge.quorvex { left: 332px; }
  .social-dot {
    position: absolute; top: 143px; width: 20px; height: 20px; border-radius: 50%;
    background: var(--navy); border: 1px solid rgba(255,255,255,.5);
  }
  .social-dot svg { position: absolute; left: 4px; top: 4px; }
  .indicia {
    position: absolute; left: 615px; top: 14px; width: 58px; height: 57px;
    background: var(--white); color: var(--ink);
    font-family: "Arimo", Arial, sans-serif; font-size: 7.6px; line-height: 9.4px;
    text-align: center; padding-top: 4px;
  }
  .indicia b { font-weight: 700; }
  .address-box {
    position: absolute; left: 459px; top: 98px; width: 196px; height: 77px;
    background: var(--white); color: var(--ink);
    font-family: "Arimo", Arial, sans-serif;
  }
  .address-box .route { position: absolute; right: 14px; top: 13px; font-size: 9px; }
  .address-box .recipient { position: absolute; left: 14px; top: 36px; font-size: 11.5px; line-height: 13px; }

  /* ---------- back ---------- */
  .back { top: 618px; height: 489px; background: var(--navy); }
  .back-corner {
    position: absolute; left: 528px; top: 0; width: 172px; height: 334px;
    background: var(--green-bright);
  }
  .back-panel {
    position: absolute; left: 34px; top: 26px; width: 424px; height: 308px;
    background: linear-gradient(100deg, var(--green) 0%, #4fb07d 50%, var(--teal) 100%);
  }
  .benefit-list {
    list-style: none; position: absolute; left: 28px; top: 20px; width: 360px;
    color: var(--white); font-size: 11.8px; line-height: 14px;
  }
  .benefit-list li { position: relative; padding-left: 9px; margin-bottom: 14.5px; }
  .benefit-list li::before {
    content: ""; position: absolute; left: 0; top: 5px; width: 4px; height: 4px; background: var(--white);
  }
  .benefit-list strong { font-weight: 700; }
  .savings-card {
    position: absolute; left: 458px; top: 26px; width: 212px; height: 308px;
    background: var(--white); color: var(--navy); text-align: center;
  }
  .savings-lead { margin-top: 18px; font-size: 13.4px; }
  .savings-figure { font-size: 24px; font-weight: 700; line-height: 28px; margin-top: 2px; }
  .savings-figure small { font-size: 13px; }
  .savings-body { font-size: 13.4px; line-height: 19.5px; }
  .savings-cta { margin-top: 18px; font-size: 10.8px; line-height: 15.5px; }
  .savings-meter {
    position: absolute; left: 15px; top: 230px; width: 182px; height: 56px;
    background: linear-gradient(90deg, var(--copper) 0%, var(--silver) 45%, var(--gold) 100%);
    opacity: .85;
  }
  .back-footer-brand {
    position: absolute; left: 0; top: 334px; width: 227px; height: 155px; background: var(--navy);
  }
  .back-footer-brand .brand-lockup { left: 38px; top: 48px; font-size: 25px; }
  .back-footer-brand .brand-lockup .dot { width: 15px; height: 15px; }
  .back-footer-brand .footer-web {
    position: absolute; left: 0; width: 227px; top: 124px; text-align: center;
    color: var(--white); font-size: 10.5px; font-weight: 500;
  }
  .services {
    position: absolute; left: 227px; top: 334px; width: 473px; height: 155px;
    background: var(--green-bright);
  }
  .services-title {
    position: absolute; left: 23px; top: 15px; white-space: pre;
    color: var(--pale); font-size: 15.2px; font-weight: 700; letter-spacing: -0.1px;
  }
  .services-col {
    list-style: none; position: absolute; top: 45px;
    color: var(--pale); font-size: 11.8px; line-height: 19.6px;
  }
  .services-col li::before { content: "▸ "; font-size: 7px; color: var(--navy); vertical-align: 2px; }
  .services-col.first { left: 23px; }
  .services-col.second { left: 205px; }
</style>
</head>
<body>

<!-- Front of mailer -->
<section class="card front">
  <div class="front-hero">
    <h1 class="front-headline">
      <span class="line-1">As more of your neighbors sign up,</span>
      <span class="line-2">your price goes down!</span>
    </h1>
    <p class="front-intro">Here at <strong>YardMint</strong>, we not only bring the convenience of selecting and scheduling all of your landscaping service needs right to your fingertips, but we pair our local team with you and your neighbors utilizing our proven technology. Which by the way, <strong>saves you time and money!</strong></p>
  </div>
  <div class="front-stripe"></div>
  <div class="front-band" role="img" aria-label="Faint photo of a neighborhood street behind a green to teal gradient">
    <div class="brand-lockup"><span class="dot"></span>YardMint</div>
    <div class="front-web">www.YardMint.example</div>
    <div class="store-badge plinth">Plinth Store</div>
    <div class="store-badge quorvex">Quorvex Apps</div>
    <span class="social-dot" style="left:267px"></span>
    <span class="social-dot" style="left:316px"></span>
    <span class="social-dot" style="left:366px">
      <svg width="12" height="12" viewBox="0 0 12 12" fill="none" stroke="#fff" stroke-width="1.4" stroke-linecap="round">
        <path d="M5 7 L7 5"/><path d="M4.2 5.6 L3 6.8 a1.8 1.8 0 0 0 2.5 2.5 L6.7 8"/><path d="M7.8 6.4 L9 5.2 a1.8 1.8 0 0 0 -2.5 -2.5 L5.3 3.9"/>
      </svg>
    </span>
    <div class="indicia">PRSRT STD<br>ECRWSS<br>U.S. Postage<br><b>PAID</b><br>RCMX RETAIL</div>
    <div class="address-box">
      <span class="route">*****************ECRWSS****</span>
      <span class="recipient">Local<br>Postal Customer</span>
    </div>
  </div>
</section>

<!-- Back of mailer -->
<section class="card back">
  <div class="back-corner"></div>
  <div class="back-panel" role="img" aria-label="Faint photo of a suburban home behind a green to teal gradient">
    <ul class="benefit-list">
      <li>We are licensed and insured landscaping pros</li>
      <li>Real, instant, upfront pricing for mowing, mulching<br>and most other services</li>
      <li>Sign up with a few easy steps and manage your<br>account from our app or online</li>
      <li>Automated safe &amp; secure transactions upon service<br>completion and satisfaction</li>
      <li>Excellent customer service with our quality<br>guaranteed commitment!</li>
      <li>Sign up now and receive <strong>50%</strong> off your first mow!</li>
      <li>Veteran owned</li>
      <li>A portion of our proceeds go to "Rowan Ellery Foundation"</li>
    </ul>
  </div>
  <div class="savings-card">
    <p class="savings-lead">You could save up to</p>
    <p class="savings-figure">10%<small> off</small></p>
    <p class="savings-body">our already low prices,<br>as more of your<br>neighbors sign up!</p>
    <p class="savings-cta">Check out our App today to<br>see how much your neighbors<br>are already saving!</p>
    <div class="savings-meter" role="img" aria-label="Illustration of the neighborhood savings barometer rising from 5 to 10 percent"></div>
  </div>
  <div class="back-footer-brand">
    <div class="brand-lockup"><span class="dot"></span>YardMint</div>
    <div class="footer-web">www.YardMint.example</div>
  </div>
  <div class="services">
    <h2 class="services-title">LIST'S OUT ALL OF THE  SERVICES WE WILL OFFER:</h2>
    <ul class="services-col first">
      <li>Mowing</li>
      <li>Mulching</li>
      <li>Aeration and Over-seeding</li>
      <li>Fertilization</li>
      <li>Shrub/Tree Trimming</li>
    </ul>
    <ul class="services-col second">
      <li>Leaf removal and yard clean up</li>
      <li>Accent lighting installation</li>
      <li>Sprinkler blow-out / Winterization</li>
      <li>Driveway pressure washing and sealing</li>
      <li>Firewood Delivery</li>
    </ul>
  </div>
</section>

</body>
</html>
```